Harlow Ironworks Business Card

We need a business card design for a new small metal fabrication business in rural NSW, Australia.

The business (Harlow Ironworks) is owner operated by a man with the initials KB - much of the branding comes from this name.

Harlow Ironworks designs, engineers, repairs and manufactures a range of custom, quality metal works including vehicle trays, agricultural machinery impliments, trailers, wood splitters, fire pits, furniture etc.

The brand position focuses on custom work of the highest quality.

Business card design should show quality, attention to detail and stand out among a mass of business cards.

Logos are in the files

The grey color may be changed on the logo if required to stand out more.

There is an image attached of a simple card that is liked because it is clean, clear, simple, masculine and effective. It says 'quality'. As most of the work we do is custom it would be good to have the business card speak to this.

Target Market(s)

Rural and regional based Australians. Primarily adult male 25-60 yrs. Primary production / rural / travelling lifestyle.

Industry/Entity Type

Metal Fabrication

Contact Information for Business Card

The words 'custom quality fabrications' would be great somewhere perhaps on the backside (not on the information side)
Name
title
Phone: 0418 539 746 and (02) 6193 4827
email: info@harlowiw.com.au
www.harlowiw.com.au

address (2 lines)

Requirements
Nice to have
• Background colour should be very navy blue or black.
Should not have
• NO orange and blue combinations.
• Navy is OK

```html
<!DOCTYPE html>
<html lang="en">
<head>
<meta charset="utf-8">
<title>Harlow Ironworks – Business Card</title>
<link href="https://fonts.googleapis.com/css2?family=PT+Sans:wght@400;700&display=swap" rel="stylesheet">
<style>
  :root {
    --navy: #14156a;
    --green: #69bd45;
    --ink: #2a2a2a;
    --card: #ffffff;
    --backdrop: #e6e7ea;
  }
  * { margin: 0; padding: 0; box-sizing: border-box; }
  html, body {
    width: 1200px;
    height: 900px;
    overflow: hidden;
    background: var(--backdrop);
    font-family: "PT Sans", Arial, sans-serif;
  }
  .card {
    position: absolute;
    left: 220px;
    top: 215px;
    width: 760px;
    height: 470px;
    background: var(--card);
    border-radius: 6px 235px 235px 6px;
    box-shadow: 0 10px 30px rgba(0,0,0,0.12);
  }
  .accent-bar {
    position: absolute;
    left: 0;
    top: 98px;
    width: 18px;
    height: 249px;
    background: var(--green);
  }
  .contact-block {
    position: absolute;
    left: 56px;
    top: 94px;
    color: var(--ink);
  }
  .holder-name {
    font-size: 31px;
    font-weight: 700;
    color: var(--navy);
    line-height: 1.1;
  }
  .holder-title {
    font-size: 20px;
    margin-top: 6px;
  }
  .contact-list {
    list-style: none;
    margin-top: 22px;
  }
  .contact-list li {
    display: flex;
    align-items: center;
    font-size: 20px;
    line-height: 28px;
  }
  .contact-list svg {
    width: 15px;
    height: 15px;
    margin-right: 12px;
    fill: var(--navy);
    flex: none;
  }
  .address {
    font-size: 20px;
    line-height: 25px;
    margin-top: 14px;
    margin-left: 4px;
  }
  .brand {
    position: absolute;
    left: 392px;
    top: 108px;
    width: 264px;
    display: flex;
    flex-direction: column;
    align-items: center;
  }
  .brand-mark {
    width: 120px;
    height: 120px;
    background: var(--green);
  }
  .brand-name {
    margin-top: 30px;
    font-size: 34px;
    font-weight: 700;
    color: var(--navy);
    text-align: center;
    line-height: 1.05;
    letter-spacing: 1px;
    text-transform: uppercase;
  }
</style>
</head>
<body>
  <div class="card">
    <div class="accent-bar"></div>

    <div class="contact-block">
      <h1 class="holder-name">Kieran Blake</h1>
      <p class="holder-title">Managing Director</p>
      <ul class="contact-list">
        <li><svg viewBox="0 0 16 16" aria-hidden="true"><path d="M1 5c0-2 3-3 7-3s7 1 7 3v1h-3V5H4v1H1zM4 7h8l2 7H2z"/></svg>0418 539 746</li>
        <li><svg viewBox="0 0 16 16" aria-hidden="true"><path d="M1 5c0-2 3-3 7-3s7 1 7 3v1h-3V5H4v1H1zM4 7h8l2 7H2z"/></svg>(02) 6193 4827</li>
        <li><svg viewBox="0 0 16 16" aria-hidden="true"><path d="M1 3h14v10H1zM2 4l6 5 6-5v1L8 10 2 5z" fill-rule="evenodd"/></svg>info@harlowiw.com.au</li>
        <li><svg viewBox="0 0 16 16" aria-hidden="true"><circle cx="8" cy="8" r="7"/></svg>www.harlowiw.com.au</li>
      </ul>
      <p class="address">1234, Address Goes Here<br>Country Name, 123456</p>
    </div>

    <div class="brand">
      <div class="brand-mark"></div>
      <p class="brand-name">Harlow Ironworks</p>
    </div>
  </div>
</body>
</html>
```